Business Card Design Project - bel soravin group

dear Sirs

we need business card design for our group ( BEL Soravin Group ) , i have got the Logo design of our group from pixel harbor in previous , so all need details relating to our group i think available with you, as well as the the chosen logo design

we hope to provide us with business card logo that to be appropaite and satisfactory to us .

thanks

note : logo design of our group is attached .
Updates

Reason: please extend the deadline of my project for additional 15 days because i didn't received appropriate design for our gruop yet . kindly beaware that i have received 77 design till now , supossed to send me 200-250 design at least . thanks

Target Market(s)

contents
-

name : Korvan EL Mistrani

position : Operation Manager

Industry/Entity Type

Business

Requirements
Must have

• person name

group logo
Nice to have
• logo color matching with back background

```html
<!DOCTYPE html>
<html lang="en">
<head>
<meta charset="utf-8">
<title>BEL Soravin Group – Business Card</title>
<link rel="stylesheet" href="https://fonts.googleapis.com/css2?family=Jost:ital,wght@0,400;0,500;1,700&display=swap">
<style>
  :root {
    --brand-blue: #0f4f94;
    --brand-gold: #cbb56c;
    --card-white: #f4f5f7;
    --page-bg: #e4e2de;
    --text-blue: #163f7a;
  }
  * { box-sizing: border-box; margin: 0; padding: 0; }
  html, body { width: 1200px; height: 880px; overflow: hidden; }
  body {
    background: var(--page-bg);
    font-family: "Jost", "Helvetica Neue", Arial, sans-serif;
    position: relative;
  }
  .card {
    position: absolute;
    width: 540px;
    height: 310px;
    background: var(--card-white);
    box-shadow: 0 4px 14px rgba(0,0,0,0.18);
    overflow: hidden;
  }
  .card--front { left: 40px; top: 285px; }
  .card--back {
    left: 620px; top: 285px;
    border-left: 14px solid var(--brand-blue);
    border-right: 14px solid var(--brand-blue);
    display: flex; align-items: center; justify-content: center;
  }

  /* Front card */
  .front__header {
    position: absolute; left: 0; top: 0;
    width: 100%; height: 148px;
    background: var(--brand-blue);
    display: flex; align-items: center; justify-content: center;
  }
  .brand {
    display: flex; align-items: center; gap: 14px;
    font-weight: 500;
    letter-spacing: 1px;
    text-transform: uppercase;
    white-space: nowrap;
  }
  .brand__mark { width: 26px; height: 26px; flex: none; }
  .brand--light { color: #ffffff; font-size: 32px; }
  .brand--light .brand__mark { background: #ffffff; }
  .brand--dark { color: var(--brand-blue); font-size: 34px; }
  .brand--dark .brand__mark { background: var(--brand-blue); width: 28px; height: 28px; }

  .front__nameband {
    position: absolute; left: 0; top: 156px;
    width: 100%; height: 40px;
    background: var(--brand-gold);
    display: flex; align-items: center; justify-content: center; gap: 14px;
    color: var(--text-blue);
  }
  .person__name { font-weight: 700; font-style: italic; font-size: 20px; }
  .person__role { font-size: 15px; }
  .person__role::before { content: "| "; }

  .contacts {
    position: absolute; top: 222px; left: 0; width: 100%;
    display: flex; justify-content: space-between;
    padding: 0 34px 0 42px;
    color: var(--text-blue);
    font-size: 15px;
    line-height: 22px;
  }
  .contacts__list { list-style: none; }
  .contacts__list li { display: flex; gap: 6px; }
  .contacts__label { display: inline-block; text-align: right; }
  .contacts__list--phones .contacts__label { width: 40px; }
  .contacts__list--web .contacts__label { width: 70px; }
</style>
</head>
<body>
  <section class="card card--front" aria-label="Business card front">
    <header class="front__header">
      <div class="brand brand--light">
        <span class="brand__mark"></span>
        <span class="brand__name">BEL Soravin Group</span>
      </div>
    </header>
    <div class="front__nameband">
      <span class="person__name">Korvan EL Mistrani</span>
      <span class="person__role">Operation Manager</span>
    </div>
    <div class="contacts">
      <ul class="contacts__list contacts__list--phones">
        <li><span class="contacts__label">Tel :</span><span>+00 123 456 789</span></li>
        <li><span class="contacts__label">Fax :</span><span>+00 123 456 789</span></li>
        <li><span class="contacts__label">Mob :</span><span>+00 123 456 789</span></li>
      </ul>
      <ul class="contacts__list contacts__list--web">
        <li><span class="contacts__label">Email :</span><span>korvan@belsoravingroup.com</span></li>
        <li><span class="contacts__label">Website :</span><span>belsoravingroup.com</span></li>
        <li><span class="contacts__label">PO. Box :</span><span>Your PO Box Number</span></li>
      </ul>
    </div>
  </section>

  <section class="card card--back" aria-label="Business card back">
    <div class="brand brand--dark">
      <span class="brand__mark"></span>
      <span class="brand__name">BEL Soravin Group</span>
    </div>
  </section>
</body>
</html>
```